Software Engineering Company need eye catching banner for and Engineering conventions

We need an eye-catching banner designed. The size of the banner will be 34" W x 81" H. We develop routing software installed in bus systems and use GPS real-time tracking to always know where they are. We would like the banner to be dominated by the colors in our logo, 2 different blues, dark gray and of course white and black if needed. We are hoping for something that will pop out and look awesome. If you want to use our entire name or just our logo is completely up to you.

Target Market(s)

Young Engineers looking for new and cutting edge job opportunities

Industry/Entity Type

Computer Software

Colors
1f68ae
3779b6
ffffff

Requirements
Should not have
• the colors in our logo

```html
<!DOCTYPE html>
<html lang="en">
<head>
<meta charset="utf-8">
<title>Veltran Technologies – Future Forward</title>
<link rel="stylesheet" href="https://fonts.googleapis.com/css2?family=Montserrat:wght@500;600;800&family=Roboto+Condensed:wght@400;700&family=Tinos&display=swap">
<style>
  :root {
    --blue-main: #1f68ae;
    --blue-light: #3779b6;
    --navy: #0c1a33;
    --navy-deep: #081329;
    --black: #000000;
    --white: #ffffff;
    --gray-text: #555555;
    --gray-rule: #5a5a5a;
    --cloud-gray: #d9dbe0;
    --cloud-light: #eef0f3;
  }
  * { box-sizing: border-box; margin: 0; padding: 0; }
  html, body { width: 686px; height: 1200px; overflow: hidden; background: var(--white); }
  .banner {
    position: relative; width: 686px; height: 1200px; overflow: hidden;
    background: var(--navy);
    font-family: "Roboto Condensed", sans-serif;
  }

  /* Hero photograph area */
  .hero-visual {
    position: absolute; left: 0; top: 0; width: 686px; height: 460px;
    background:
      radial-gradient(ellipse 60% 40% at 58% 52%, rgba(120,190,230,0.45) 0%, rgba(40,110,160,0.25) 45%, rgba(0,0,0,0) 75%),
      radial-gradient(ellipse 35% 25% at 18% 62%, rgba(190,150,130,0.35) 0%, rgba(0,0,0,0) 70%),
      linear-gradient(to bottom, #0b1a30 0%, #123a5a 35%, #0f3350 60%, #050b14 100%);
  }

  /* Brand tab */
  .brand-tab { position: absolute; left: 130px; top: 8px; width: 422px; height: 168px; }
  .brand-tab svg { position: absolute; inset: 0; }
  .brand-name {
    position: absolute; left: 34px; top: 26px; display: flex; align-items: center; gap: 14px;
    font-family: "Montserrat", sans-serif; font-weight: 800; color: var(--blue-main);
  }
  .brand-mark { width: 50px; height: 50px; background: var(--blue-main); flex: none; }
  .brand-words { line-height: 1; }
  .brand-words .main { font-size: 50px; letter-spacing: 1px; display: block; }
  .brand-words .sub { font-size: 14.5px; letter-spacing: 5.4px; display: block; margin-top: 6px; }
  .brand-url {
    position: absolute; left: 98px; top: 106px;
    font-family: "Montserrat", sans-serif; font-weight: 500; font-size: 10.5px;
    letter-spacing: 3.3px; color: var(--gray-text);
  }

  /* Headline band */
  .headline-band { position: absolute; left: 0; top: 453px; width: 686px; height: 185px; }
  .headline-band svg { position: absolute; inset: 0; }
  .rule { position: absolute; left: 68px; width: 550px; height: 2px; background: var(--white); }
  .rule::before, .rule::after {
    content: ""; position: absolute; top: -5px; width: 12px; height: 12px;
    border-radius: 50%; background: var(--white);
  }
  .rule::before { left: -6px; } .rule::after { right: -6px; }
  .rule-top { top: 14px; } .rule-bottom { top: 90px; }
  .headline {
    position: absolute; left: 0; right: 0; top: 20px; text-align: center;
    font-family: "Tinos", serif; font-weight: 400; font-size: 65px; line-height: 68px;
    color: var(--white); letter-spacing: 0.5px; white-space: nowrap;
  }
  .intro {
    position: absolute; left: 0; right: 0; top: 106px; text-align: center;
    font-family: "Montserrat", sans-serif; font-weight: 600; font-size: 19.5px;
    line-height: 23px; color: var(--white); white-space: nowrap;
  }

  /* Feature rows */
  .feature { position: absolute; left: 0; width: 686px; height: 90px; }
  .feature-bar {
    position: absolute; top: 30px; height: 30px; background: var(--white);
    font-weight: 700; font-size: 23px; line-height: 30px; color: var(--navy);
    text-align: center;
  }
  .feature-icon {
    position: absolute; top: 5px; width: 80px; height: 80px; border-radius: 50%;
    background: var(--white); display: flex; align-items: center; justify-content: center;
  }
  .feature-text {
    position: absolute; font-size: 16px; line-height: 17px; color: var(--white);
  }
  .feature.is-left .feature-bar { left: 0; width: 215px; padding-right: 24px; }
  .feature.is-left .feature-icon { left: 200px; }
  .feature.is-left .feature-text { left: 316px; width: 332px; }
  .feature.is-right .feature-bar { left: 420px; width: 266px; padding-left: 30px; }
  .feature.is-right .feature-icon { left: 372px; }
  .feature.is-right .feature-text { left: 34px; width: 322px; }
  .feature-technology { top: 643px; }
  .feature-technology .feature-text { top: 8px; }
  .feature-cloud { top: 753px; }
  .feature-cloud .feature-text { top: 9px; }
  .feature-gps { top: 851px; }
  .feature-gps .feature-text { top: 17px; }
  .feature-secure { top: 951px; }
  .feature-secure .feature-text { top: 19px; }

  /* Footer illustration area and call to action */
  .cloud-footer {
    position: absolute; left: 0; top: 1040px; width: 686px; height: 160px;
    background: linear-gradient(to bottom,
      rgba(12,26,51,0) 0%, var(--cloud-gray) 32%, var(--cloud-light) 58%, var(--white) 80%);
  }
  .call-bar {
    position: absolute; left: 166px; top: 1137px; width: 520px; height: 32px;
    background: var(--navy); border-radius: 16px 0 0 16px;
    font-weight: 700; font-size: 33px; line-height: 33px; color: var(--white);
    text-align: center; white-space: nowrap;
  }
</style>
</head>
<body>
<main class="banner">
  <div class="hero-visual" role="img" aria-label="A hand reaching toward a glowing network of technology icons — servers, cloud, phones, laptops and security shields — over a blurred city at night"></div>

  <header class="brand-tab">
    <svg width="422" height="168" viewBox="0 0 422 168">
      <polygon points="0,0 422,0 422,160 211,130 0,160" fill="#ffffff"/>
      <polyline points="28,164 211,136 394,164" fill="none" stroke="#5a5a5a" stroke-width="4"/>
    </svg>
    <div class="brand-name">
      <span class="brand-mark"></span>
      <span class="brand-words"><span class="main">VELTRAN</span><span class="sub">TECHNOLOGIES LLC</span></span>
    </div>
    <div class="brand-url">www.veltrantechnologies.com</div>
  </header>

  <section class="headline-band">
    <svg width="686" height="185" viewBox="0 0 686 185">
      <polygon points="0,0 686,0 686,163 343,185 0,163" fill="#000000"/>
    </svg>
    <div class="rule rule-top"></div>
    <h1 class="headline">FUTURE FORWARD</h1>
    <div class="rule rule-bottom"></div>
    <p class="intro">We develop routing software installed in bus systems and<br>use GPS real-time tracking to always know where they are.</p>
  </section>

  <section class="feature is-left feature-technology">
    <div class="feature-bar">TECHNOLOGY</div>
    <div class="feature-icon">
      <svg width="48" height="40" viewBox="0 0 48 40">
        <rect x="6" y="10" width="34" height="22" rx="2" fill="none" stroke="#0c1a33" stroke-width="3"/>
        <path d="M1 35h46l-3 4H4z" fill="#0c1a33"/>
        <rect x="30" y="2" width="6" height="6" fill="#0c1a33"/>
        <rect x="40" y="0" width="6" height="6" fill="#0c1a33"/>
        <rect x="26" y="12" width="5" height="5" fill="#0c1a33"/>
        <rect x="34" y="16" width="5" height="5" fill="#0c1a33"/>
        <rect x="20" y="20" width="4" height="4" fill="#0c1a33"/>
      </svg>
    </div>
    <p class="feature-text">We implement the latest innovations in transportation technology. This gives us the ability to provide you with reliable, accurate data when you need it most.</p>
  </section>

  <section class="feature is-right feature-cloud">
    <p class="feature-text">We use state of the art cloud technology to store and process your day to day operations. Your data is always just a few clicks away.</p>
    <div class="feature-bar">CLOUD</div>
    <div class="feature-icon">
      <svg width="56" height="36" viewBox="0 0 56 36">
        <path d="M12 34a10 10 0 0 1-1-20 14 14 0 0 1 27-4 11 11 0 0 1 8 24z" fill="#0c1a33"/>
      </svg>
    </div>
  </section>

  <section class="feature is-left feature-gps">
    <div class="feature-bar">GPS</div>
    <div class="feature-icon">
      <svg width="54" height="46" viewBox="0 0 54 46">
        <path d="M4 34l22-10 24 8-22 12z" fill="none" stroke="#0c1a33" stroke-width="3" stroke-linejoin="round"/>
        <path d="M27 30c-7-9-11-14-11-19a11 11 0 0 1 22 0c0 5-4 10-11 19z" fill="#0c1a33"/>
        <circle cx="27" cy="11" r="4.5" fill="#ffffff"/>
      </svg>
    </div>
    <p class="feature-text">GPS tracking gives you the real-time information necessary to keep your vehicles on the road and on-time.</p>
  </section>

  <section class="feature is-right feature-secure">
    <p class="feature-text">With the latest security protocols in place, you can be rest assured that your data is safe.</p>
    <div class="feature-bar">SECURE</div>
    <div class="feature-icon">
      <svg width="36" height="44" viewBox="0 0 36 44">
        <path d="M8 18v-6a10 10 0 0 1 20 0v6" fill="none" stroke="#0c1a33" stroke-width="4.5"/>
        <rect x="2" y="17" width="32" height="26" rx="4" fill="#0c1a33"/>
        <circle cx="18" cy="28" r="3.5" fill="#ffffff"/>
        <rect x="16.5" y="29" width="3" height="7" fill="#ffffff"/>
      </svg>
    </div>
  </section>

  <div class="cloud-footer" role="img" aria-label="Soft gray and white clouds rising along the bottom edge of the banner"></div>

  <div class="call-bar">CALL US TODAY - 512.555.0148</div>
</main>
</body>
</html>
```